Postcard needed for expert witness service

Looking for a professional postcard that will be mailed to personal injury lawyers / law firms to introduce my expert witness services.

Target Market(s)

Law firms, personal injury lawyers

Industry/Entity Type

Expert witness, law

Font styles to use
Sans Serif

Requirements
Must have
• Logo: The Frost Counsel [Main Heading]Do you handle snow and ice related slip and falls? Darrel is one of the top snow industry experts in the country! [Following should be in a list type fashion, possibly bulleted]Darrel's credentials: Accredited Winter Practitioner (AWP), past WRTA board member and chair, former ISO 9001 certified snow company owner , 32 years in the industry. (555) 284-3917 NOTES: Postcard will be 4" x 6" Please use both sides however must have room for labels and stamp
Should not have
• Wouldn't suggest using both photos on same side. Honestly, feel free to only use one of the slip and fall photos if it works out better. Thanks!

```html
<!DOCTYPE html>
<html lang="en">
<head>
<meta charset="utf-8">
<title>The Frost Counsel – Postcard</title>
<link rel="stylesheet" href="https://fonts.googleapis.com/css2?family=Source+Sans+3:ital,wght@0,400;0,500;1,400;1,700&display=swap">
<style>
  :root {
    --page: #ffffff;
    --ink-blue: #0e3a8f;
    --ink-dark: #141414;
    --white: #ffffff;
    --front-photo-top: #a3bcda;
    --front-photo-mid: #6f8fbf;
    --front-photo-low: #2c4372;
    --front-panel: rgba(118, 137, 173, 0.95);
    --front-band: rgba(24, 44, 92, 0.75);
    --back-base: #b7cbdd;
    --back-photo: #a9bfd5;
  }
  * { margin: 0; padding: 0; box-sizing: border-box; }
  html, body { width: 1000px; height: 1200px; overflow: hidden; background: var(--page); }
  body { position: relative; font-family: "Source Sans 3", sans-serif; }

  .card { position: absolute; left: 190px; width: 620px; height: 414px; overflow: hidden; }
  .card--front { top: 151px; }
  .card--back { top: 634px; background: var(--back-base); }

  .abs { position: absolute; line-height: 1; white-space: nowrap; }

  /* front */
  .front-photo { position: absolute; inset: 0;
    background: linear-gradient(160deg, var(--front-photo-top) 0%, var(--front-photo-mid) 55%, var(--front-photo-low) 100%); }
  .front-panel { position: absolute; inset: 0; }
  .front-band { position: absolute; left: 0; right: 0; top: 328px; bottom: 0; background: var(--front-band); }
  .front-frame { position: absolute; left: 12.5px; top: 12.5px; right: 12.5px; bottom: 12.5px; border: 1.5px solid var(--white); }

  .headline { color: var(--ink-blue); font-weight: 400; }
  .headline--lead { left: 26px; top: 26px; font-size: 48px; }
  .headline--line { left: 26px; font-size: 33px; }
  .intro { left: 27px; font-size: 26px; color: var(--white); }
  .intro strong { font-weight: 700; font-style: italic; }

  .brand { color: var(--ink-dark); font-weight: 500; font-size: 28px; letter-spacing: 2px; }

  .phone { display: flex; align-items: center; gap: 8px; font-weight: 400; }
  .phone svg { flex: none; }
  .phone--front { left: 356px; top: 357px; font-size: 27px; color: var(--white); letter-spacing: 0.5px; }

  /* back */
  .back-photo { position: absolute; left: 0; top: 0; width: 310px; height: 100%;
    background: linear-gradient(170deg, var(--back-base) 0%, var(--back-photo) 45%, #bccfe0 100%); }
  .brand--back { left: 0; width: 620px; text-align: center; }
  .stamp-box { position: absolute; left: 496px; top: 25px; width: 103px; height: 129px;
    border: 1.5px dashed var(--ink-blue); display: flex; align-items: center; justify-content: center; }
  .stamp-box span { color: var(--ink-blue); font-style: italic; font-size: 24px; }

  .credentials-title { left: 25px; top: 145px; font-size: 25px; font-weight: 700; font-style: italic; color: var(--ink-blue); }
  .credentials { position: absolute; left: 25px; top: 200px; width: 290px; list-style: none; color: var(--ink-blue); font-size: 16.5px; line-height: 21px; }
  .credentials li { position: relative; padding-left: 16px; margin-bottom: 8.5px; }
  .credentials li::before { content: ""; position: absolute; left: 2px; top: 9px; width: 5px; height: 5px; border-radius: 50%; background: var(--ink-blue); }
  .phone--back { left: 25px; top: 362px; font-size: 29px; color: var(--ink-blue); letter-spacing: 0.5px; }

  .address-line { position: absolute; left: 322px; width: 277px; height: 1px; background: var(--ink-blue); }
</style>
</head>
<body>

<section class="card card--front">
  <div class="front-photo" role="img" aria-label="Photograph of a person slipping and falling on an icy sidewalk"></div>
  <svg class="front-panel" width="620" height="414" viewBox="0 0 620 414" aria-hidden="true">
    <polygon points="0,0 229,0 338,414 0,414" fill="var(--front-panel)"/>
  </svg>
  <div class="front-band"></div>
  <div class="front-frame"></div>

  <h1 class="abs headline headline--lead">Do you</h1>
  <p class="abs headline headline--line" style="top:76px">handle snow</p>
  <p class="abs headline headline--line" style="top:115px">and ice related</p>
  <p class="abs headline headline--line" style="top:154px">slip and falls?</p>

  <p class="abs intro" style="top:217px"><strong>Darrel</strong> is one of</p>
  <p class="abs intro" style="top:250px">the top snow industry</p>
  <p class="abs intro" style="top:283px">experts in the country!</p>

  <p class="abs brand" style="left:27px; top:338px">THE FROST</p>
  <p class="abs brand" style="left:27px; top:366px">COUNSEL</p>

  <p class="abs phone phone--front">
    <svg width="22" height="22" viewBox="0 0 24 24" aria-hidden="true"><path fill="currentColor" d="M6.6 10.8c1.4 2.8 3.8 5.1 6.6 6.6l2.2-2.2c.3-.3.7-.4 1-.2 1.1.4 2.3.6 3.6.6.6 0 1 .4 1 1V20c0 .6-.4 1-1 1C10.6 21 3 13.4 3 4c0-.6.4-1 1-1h3.5c.6 0 1 .4 1 1 0 1.3.2 2.5.6 3.6.1.3 0 .7-.2 1l-2.3 2.2z"/></svg>
    (555) 284-3917
  </p>
</section>

<section class="card card--back">
  <div class="back-photo" role="img" aria-label="Faint photograph of a person fallen on snowy ground"></div>

  <p class="abs brand brand--back" style="top:27px">THE FROST</p>
  <p class="abs brand brand--back" style="top:53px">COUNSEL</p>

  <div class="stamp-box"><span>STAMP</span></div>

  <h2 class="abs credentials-title">Darrel's credentials</h2>
  <ul class="credentials">
    <li>Accredited Winter Practitioner (AWP).</li>
    <li>Past WRTA board member and chair.</li>
    <li>Former ISO 9001 certified snow company owner.</li>
    <li>32 years in the industry.</li>
  </ul>

  <p class="abs phone phone--back">
    <svg width="22" height="22" viewBox="0 0 24 24" aria-hidden="true"><path fill="currentColor" d="M6.6 10.8c1.4 2.8 3.8 5.1 6.6 6.6l2.2-2.2c.3-.3.7-.4 1-.2 1.1.4 2.3.6 3.6.6.6 0 1 .4 1 1V20c0 .6-.4 1-1 1C10.6 21 3 13.4 3 4c0-.6.4-1 1-1h3.5c.6 0 1 .4 1 1 0 1.3.2 2.5.6 3.6.1.3 0 .7-.2 1l-2.3 2.2z"/></svg>
    (555) 284-3917
  </p>

  <div class="address-line" style="top:240px"></div>
  <div class="address-line" style="top:283px"></div>
  <div class="address-line" style="top:326px"></div>
  <div class="address-line" style="top:369px"></div>
</section>

</body>
</html>
```